R7M Meridian Business Card Design

We need a business card created for our New Business "R7M Meridian"<br/><br/>The business card design is up to you however the following information must be on the business card:<br/><br/>Front of the business card -<br/>Email :dorianv@r7mmeridian.nz<br/>Mobile: +64 (0) 22 4871 659<br/>Website: www.r7mmeridian.nz<br/>Card Owner Name: Dorian Valcourt<br/>Company Title: Business Development Manager<br/>Slogan: "The BEST of both worlds". <br/>Logo On the front attached to the design brief<br/><br/>On the back: <br/>Space on the back for 4 more versions of the logo across the bottom of the card indicating different subsidiary brands - R7M Coffee, R7M Arts, R7M ?? (The card will be used for all of these brands - We Will add the extra subsidiary logos to the design once the design is finished (We are a graphics design team). <br/><br/>Other than that we want a premium feeling logo that remains universally usable depending on the business entity that we are using the card for. The use of bright bold colours would be great but we still want the card to feel premium.
Target Market(s)
Gift Design and Manufacturing Companies
Contact Information for Business Card
Front of the business card -
Email :dorianv@r7mmeridian.nz
Mobile: +64 (0) 22 4871 659
Website: www.r7mmeridian.nz
Card Owner Name: Dorian Valcourt
Company Title: Business Development Manager
Slogan: "The BEST of both worlds".
Logo On the front attached to the design brief

```html
<!DOCTYPE html>
<html lang="en">
<head>
<meta charset="utf-8">
<title>R7M Meridian Business Card</title>
<link href="https://fonts.googleapis.com/css2?family=Exo+2:wght@500;700&family=Open+Sans:wght@400;600&display=swap" rel="stylesheet">
<style>
  :root {
    --stage: #202123;
    --card-dark: #1b1c1e;
    --card-dark-mark: #2b2c30;
    --ring: #23264a;
    --paper: #ffffff;
    --brand-blue: #3645a0;
    --ink: #2a2a2a;
    --rule: #555555;
  }
  * { box-sizing: border-box; margin: 0; padding: 0; }
  html, body { width: 1200px; height: 900px; overflow: hidden; }
  body {
    background: var(--stage);
    font-family: "Open Sans", sans-serif;
    position: relative;
  }
  .card {
    position: absolute;
    left: 285px;
    width: 630px;
    height: 360px;
    overflow: hidden;
  }
  /* Back side */
  .card-back { top: 50px; background: var(--card-dark); }
  .back-ring {
    position: absolute;
    left: 50%; top: 50%;
    width: 300px; height: 300px;
    margin: -150px 0 0 -150px;
    border: 4px solid var(--ring);
    border-radius: 50%;
  }
  .back-name {
    position: absolute;
    left: 0; right: 0; top: 50%;
    transform: translateY(-50%);
    text-align: center;
    font-family: "Exo 2", sans-serif;
    font-weight: 700;
    font-size: 40px;
    color: var(--card-dark-mark);
    letter-spacing: 1px;
  }
  /* Front side */
  .card-front { top: 450px; background: var(--paper); }
  .brand {
    position: absolute;
    left: 40px; top: 110px;
    display: flex; align-items: center; gap: 12px;
  }
  .brand-dot {
    width: 22px; height: 22px; border-radius: 50%;
    background: var(--brand-blue);
  }
  .brand-name {
    font-family: "Exo 2", sans-serif;
    font-weight: 700;
    font-size: 30px;
    color: var(--brand-blue);
    line-height: 1;
  }
  .divider {
    position: absolute;
    left: 318px;
    width: 2px;
    background: var(--rule);
  }
  .divider-top { top: 90px; height: 40px; }
  .divider-bottom { top: 148px; height: 76px; }
  .person { position: absolute; left: 340px; top: 84px; }
  .person-name {
    font-family: "Exo 2", sans-serif;
    font-weight: 700;
    font-size: 24px;
    color: var(--brand-blue);
    letter-spacing: .5px;
    text-transform: uppercase;
  }
  .person-title { font-size: 15px; color: var(--ink); margin-top: 2px; }
  .contacts { position: absolute; left: 336px; top: 150px; list-style: none; }
  .contacts li {
    display: flex; align-items: center; gap: 10px;
    font-size: 16px; color: var(--ink); height: 24px;
  }
  .contacts svg { width: 16px; height: 16px; flex: none; }
  .slogan-band {
    position: absolute;
    left: 0; right: 0; top: 272px; height: 56px;
    background: var(--brand-blue);
    display: flex; align-items: center; justify-content: center;
  }
  .slogan {
    font-family: "Exo 2", sans-serif;
    font-weight: 500;
    font-size: 20px;
    color: var(--paper);
  }
</style>
</head>
<body>
  <section class="card card-back" aria-label="Card back">
    <div class="back-ring"></div>
    <div class="back-name">R7M Meridian</div>
  </section>

  <section class="card card-front" aria-label="Card front">
    <div class="brand">
      <span class="brand-dot"></span>
      <span class="brand-name">R7M Meridian</span>
    </div>
    <div class="divider divider-top"></div>
    <div class="divider divider-bottom"></div>
    <div class="person">
      <p class="person-name">Dorian Valcourt</p>
      <p class="person-title">Business Development Manager</p>
    </div>
    <ul class="contacts">
      <li>
        <svg viewBox="0 0 16 16" fill="none" stroke="#3645a0" stroke-width="1.4"><circle cx="8" cy="8" r="6.5"/><path d="M5.5 5c0 3 2.5 5.5 5.5 5.5l.6-1.4-1.6-.8-.8.8c-1-.4-1.9-1.3-2.3-2.3l.8-.8-.8-1.6z" stroke-linejoin="round"/></svg>
        +64 (0) 22 4871 659
      </li>
      <li>
        <svg viewBox="0 0 16 16" fill="none" stroke="#3645a0" stroke-width="1.4"><rect x="1.5" y="3.5" width="13" height="9"/><path d="M1.5 3.5 8 9l6.5-5.5"/></svg>
        dorianv@r7mmeridian.nz
      </li>
      <li>
        <svg viewBox="0 0 16 16" fill="none" stroke="#3645a0" stroke-width="1.4"><circle cx="8" cy="8" r="6.5"/><ellipse cx="8" cy="8" rx="3" ry="6.5"/><path d="M1.5 8h13M2.5 4.8h11M2.5 11.2h11"/></svg>
        www.r7mmeridian.nz
      </li>
    </ul>
    <div class="slogan-band">
      <p class="slogan">The BEST of both worlds</p>
    </div>
  </section>
</body>
</html>
```